Redesign wellness clinic website

The project is redesign a wellness clinic http://www.thornleighvitality.example. The new website is to be responsive,clean,bright and a strong call to action which is to book an appointment. The logo will remain the same but the colour scheme on the website should be reflect purple white and green. I want it to be bright and cheerful and the feeling of clarity. The website shouldn't be overloaded with content but more visuals.

Target Market(s)

Anyone that has corporate wellness benefits within the downtown Toronto core. Majority of audience are professional working in Media, Telecommunications and Investments.

Industry/Entity Type

Health And Wellness

Number of Pages Required

5+ page

Font styles to use
Sans Serif

Colors
ffffff
886aae
acd036

Requirements
Must have
• -Strong call to action which is book an appointment like this page https://www.kestrelmotion.example/
• -Services provided icons on the page like https://www.brightpathvitalityhouse.example/
• - Pictures of a good visualizing a fit and healthy life
• - Strong ratings from Quorva, Zintrel, PostMaz, similar to this website http://www.summitbalancehealth.example/our-team-professionals/
• - Bright and clear
Should not have
• -No black and white images (redo our pictures)
• -Dark themes

```html
<!DOCTYPE html>
<html lang="en">
<head>
<meta charset="utf-8">
<title>Thornleigh Vitality Centre</title>
<link href="https://fonts.googleapis.com/css2?family=Raleway:wght@400;500;600;700&family=Poppins:wght@300;400;500;600&display=swap" rel="stylesheet">
<style>
:root{
  --purple:#886aae;
  --purple-deep:#7a5ba3;
  --purple-nav:#8b6cb3;
  --purple-dark:#6f5297;
  --purple-text:#7d5fa8;
  --green:#acd036;
  --white:#ffffff;
  --ink:#3a3a3a;
  --grey:#8a8a8a;
  --line:#dcdcdc;
}
*{box-sizing:border-box;margin:0;padding:0}
html,body{width:1200px;height:2903px;overflow:hidden;background:var(--white)}
body{position:relative;font-family:"Poppins",sans-serif;color:var(--ink)}
.abs{position:absolute}
ul{list-style:none}

/* header */
.brand{left:207px;top:8px;display:flex;flex-direction:column;align-items:center;gap:3px}
.brand-mark{width:30px;height:30px;border-radius:50%;background:var(--purple)}
.brand-name{font-size:8px;color:var(--purple);font-weight:500;white-space:nowrap}
.contact-item{top:20px;display:flex;align-items:center;gap:6px;white-space:nowrap}
.contact-icon{width:26px;height:26px;border-radius:50%;background:var(--purple);display:flex;align-items:center;justify-content:center;flex:none}
.contact-text{font-size:8px;line-height:11px;color:var(--ink)}
.contact-text small{display:block;font-size:8px;color:#555}
.btn-top{left:851px;top:23px;width:126px;height:26px;border-radius:13px;background:var(--purple);color:var(--white);font-size:10px;font-weight:600;display:flex;align-items:center;gap:10px;padding-left:8px;white-space:nowrap}
.btn-top .dot{width:16px;height:16px;border-radius:50%;background:var(--white);display:flex;align-items:center;justify-content:center}

/* nav */
.nav{left:161px;top:68px;width:861px;height:42px;background:var(--purple-nav)}
.nav a{position:absolute;top:0;color:var(--white);text-decoration:none;font-family:"Raleway",sans-serif;font-weight:700;font-size:10px;letter-spacing:.2px;height:42px;line-height:42px;padding:0 11px;white-space:nowrap}
.nav a.active{background:var(--purple-dark)}

/* hero */
.hero{left:161px;top:110px;width:861px;height:350px;background:linear-gradient(90deg,#f3f6fb 0%,#eef2f8 45%,#dfe6ef 100%);overflow:hidden}
.hero-photo{position:absolute;right:0;top:0;width:540px;height:350px;background:linear-gradient(110deg,rgba(238,242,248,0) 0%,#e7d8cc 35%,#f1e6dc 60%,#e9eef4 100%)}
.hero-title{left:52px;top:74px;font-family:"Raleway",sans-serif;font-weight:700;font-size:20px;line-height:29px;color:#4a3a6a;white-space:nowrap}
.hero-title span{color:var(--purple-text)}
.hero-copy{left:52px;top:135px;width:330px;font-size:11.5px;line-height:15px;color:var(--purple-text)}
.btn-solid{background:var(--purple);color:var(--white);font-size:10.5px;font-weight:600;display:flex;align-items:center;justify-content:center;border-radius:3px;white-space:nowrap}
.hero-btn{left:52px;top:196px;width:162px;height:40px}
.hero-dots{left:426px;top:336px;display:flex;gap:6px}
.hero-dots i{width:7px;height:7px;border-radius:50%;border:1px solid #999;display:block}
.hero-dots i.on{background:#888}

/* about */
.about-photo{left:161px;top:480px;width:298px;height:371px;background:linear-gradient(180deg,#f4f6f8 0%,#e6ecf1 55%,#cfe0ea 100%)}
.about-kicker{left:536px;top:499px;font-family:"Raleway",sans-serif;font-size:25px;font-weight:500;color:#222}
.about-title{left:536px;top:530px;font-family:"Raleway",sans-serif;font-size:25px;font-weight:600;color:var(--purple-text);white-space:nowrap}
.about-rule{left:536px;top:570px;width:150px;height:1px;background:var(--purple)}
.about-copy{left:536px;top:584px;width:459px;font-size:10px;line-height:16px;color:var(--purple-text);text-align:justify}
.about-copy p+p{margin-top:16px}
.btn-outline{border:1px solid #8a8a8a;color:var(--ink);font-size:10px;display:flex;align-items:center;justify-content:center;background:var(--white);white-space:nowrap}
.about-btn{left:536px;top:780px;width:130px;height:33px}

/* services */
.services{left:161px;top:851px;width:861px;height:426px;background:linear-gradient(135deg,#8f72b6 0%,#8466ad 50%,#7c5ea6 100%)}
.section-head{font-family:"Raleway",sans-serif;font-weight:700;font-size:13px;text-align:center}
.services .section-head{position:absolute;left:0;right:0;top:32px;color:var(--white)}
.head-rule{position:absolute;height:1px;width:64px}
.services .head-rule{left:398px;top:54px;background:rgba(255,255,255,.8)}
.service{position:absolute;top:88px;width:136px;display:flex;flex-direction:column;align-items:center}
.service-icon{width:86px;height:86px;border-radius:50%;border:1.5px solid rgba(255,255,255,.85);display:flex;align-items:center;justify-content:center}
.service h3{margin-top:24px;height:34px;font-family:"Raleway",sans-serif;font-size:10.5px;font-weight:700;color:var(--white);text-align:center;line-height:14px}
.service ul{margin-top:12px;align-self:flex-start;padding-left:10px}
.service li{font-size:9.5px;line-height:18px;color:var(--white);position:relative;padding-left:12px;white-space:nowrap}
.service li::before{content:"";position:absolute;left:0;top:8px;width:3px;height:3px;border-radius:50%;background:var(--white)}

/* partners */
.partners-head{left:161px;width:861px;top:1298px;color:var(--purple-dark)}
.partners-rule{left:560px;top:1319px;background:var(--purple)}
.partner{top:1358px;width:182px;height:80px;border:1.5px solid var(--purple);display:flex;align-items:center;justify-content:center}
.partner-shape{width:100px;height:30px;border-radius:15px;background:linear-gradient(90deg,#cfe3e6,#e4dcee)}

/* banner */
.banner{left:161px;top:1484px;width:861px;height:286px;background:var(--purple);overflow:hidden}
.banner-cut{position:absolute;left:0;top:0}
.banner-photo{position:absolute;left:0;top:0;width:299px;height:286px;background:linear-gradient(160deg,rgba(255,255,255,0) 0%,#c9d3e4 40%,#b7c6de 100%);clip-path:polygon(18% 0,100% 0,100% 100%,0 100%,0 14%)}
.banner-copy{position:absolute;left:346px;top:53px;width:450px;color:var(--white)}
.banner-copy p{font-size:11px;line-height:17px}
.banner-copy .join{margin-top:12px;font-size:10.5px;font-weight:600;white-space:nowrap}
.banner-copy h2{margin-top:10px;font-family:"Raleway",sans-serif;font-weight:700;font-size:30px;line-height:41px;white-space:nowrap}
.banner-copy .mail{margin-top:4px;font-size:11px;font-weight:600;white-space:nowrap}
.banner-copy .mail u{text-underline-offset:2px}

/* blog */
.blog-head{left:203px;top:1808px;display:flex;align-items:center;gap:6px;font-family:"Raleway",sans-serif;font-size:19px;color:var(--purple-text);font-weight:500}
.blog-head b{font-size:34px;line-height:20px;font-weight:700;color:var(--purple)}
.hours{left:203px;top:1848px;width:316px;height:205px;border:2px solid #bdbdbd;outline:1px solid #bdbdbd;outline-offset:3px;padding:12px 22px}
.hours h4{font-family:"Raleway",sans-serif;font-size:13.5px;font-weight:600;color:var(--purple-text);padding-bottom:8px;border-bottom:1px solid var(--purple)}
.hours li{font-size:10px;color:var(--grey);padding:12px 0 8px;border-bottom:1px solid var(--purple);white-space:nowrap}
.hours li.closed{color:var(--ink)}
.post-title{left:544px;top:1846px;font-family:"Raleway",sans-serif;font-size:21px;font-weight:400;color:var(--purple-text)}
.post-date{left:544px;top:1882px;font-size:11px;color:var(--purple-text)}
.post-copy{left:544px;top:1904px;width:470px;font-size:13.5px;line-height:21px;color:var(--grey);text-align:justify}
.post-btn{left:548px;top:2026px;width:88px;height:27px;color:var(--grey)}
.divider{left:161px;width:861px;height:1px;background:var(--line)}

/* reviews */
.review{top:2138px;width:176px;height:82px;border:1.5px solid #9b9b9b;display:flex;flex-direction:column;align-items:center;justify-content:center}
.review .name{font-size:26px;font-weight:500;color:#5a5a5a;line-height:30px;white-space:nowrap}
.review .label{font-size:11px;color:#5a5a5a;display:flex;gap:4px;align-items:center}
.review .stars{color:#f2b600;letter-spacing:1px;font-size:10px}
.review .stars.muted{color:#bbb}

/* testimonial */
.patient-photo{left:286px;top:2303px;width:173px;height:299px;background:linear-gradient(180deg,#f6f0e6 0%,#f2e3d4 50%,#e9e6ec 100%)}
.patients-title{left:515px;top:2338px;font-family:"Raleway",sans-serif;font-size:30px;font-weight:500;color:var(--purple-text);white-space:nowrap}
.patients-rule{left:515px;top:2381px;width:92px;height:1px;background:var(--purple)}
.quote-mark{left:515px;top:2400px;font-family:"Raleway",sans-serif;font-size:40px;font-weight:700;color:var(--purple);line-height:40px}
.patients-copy{left:515px;top:2436px;width:465px;font-size:9.8px;line-height:17px;color:var(--ink)}
.patients-sign{left:518px;top:2552px;font-family:"Raleway",sans-serif;font-size:15px;font-weight:700;color:var(--purple-text)}

/* footer */
.footer{left:161px;top:2602px;width:861px;height:301px;background:linear-gradient(135deg,#8a6cb1,#7f60a8)}
.footer-bottom{position:absolute;left:0;bottom:0;width:861px;height:63px;border-top:1px solid rgba(255,255,255,.4);display:flex;align-items:center;justify-content:center;color:var(--white);font-size:10.5px}
.footer-col{position:absolute;color:var(--white);font-size:11px;line-height:15px}
.footer-about{left:50px;top:44px;width:320px;font-size:10.5px}
.contact-rows{margin-top:14px;display:grid;grid-template-columns:68px 1fr;row-gap:1px;white-space:nowrap}
.footer-col h5{font-size:12.5px;font-weight:400;margin-bottom:18px}
.links li{position:relative;padding-left:18px;line-height:17.5px;white-space:nowrap}
.links li::before{content:"";position:absolute;left:0;top:4px;width:8px;height:8px;border:1px solid var(--white);border-radius:50%}
.field{width:180px;height:25px;border:1px solid rgba(255,255,255,.8);font-size:9px;padding:0 8px;display:flex;align-items:center;margin-top:6px}
.subscribe{margin-top:14px;width:84px;height:27px;border:1px solid var(--white);border-radius:14px;font-size:10px;display:flex;align-items:center;justify-content:center}
</style>
</head>
<body>

<!-- header -->
<div class="abs brand">
  <span class="brand-mark"></span>
  <span class="brand-name">thornleigh vitality centre</span>
</div>
<div class="abs contact-item" style="left:635px">
  <span class="contact-icon"><svg width="13" height="13" viewBox="0 0 24 24"><path fill="#fff" d="M6.6 10.8a15 15 0 0 0 6.6 6.6l2.2-2.2c.3-.3.7-.4 1-.2 1.1.4 2.3.6 3.6.6.6 0 1 .4 1 1V20c0 .6-.4 1-1 1A17 17 0 0 1 3 4c0-.6.4-1 1-1h3.5c.6 0 1 .4 1 1 0 1.3.2 2.5.6 3.6.1.3 0 .7-.2 1z"/></svg></span>
  <span class="contact-text">Call us<small>0400 555 0192</small></span>
</div>
<div class="abs contact-item" style="left:736px">
  <span class="contact-icon"><svg width="13" height="13" viewBox="0 0 24 24"><path fill="#fff" d="M3 6h18v12H3z"/><path d="M3 6l9 7 9-7" stroke="#886aae" stroke-width="1.8" fill="none"/></svg></span>
  <span class="contact-text">Email<small>mail@tvc.example</small></span>
</div>
<div class="abs btn-top"><span class="dot"><svg width="10" height="10" viewBox="0 0 24 24"><circle cx="12" cy="8" r="4" fill="#886aae"/><path d="M4 21c0-4.4 3.6-7 8-7s8 2.6 8 7z" fill="#886aae"/></svg></span>Get Appointment</div>

<nav class="abs nav">
  <a class="active" style="left:80px">HOME</a>
  <a style="left:138px">FEES AND SERVICES</a>
  <a style="left:269px">OUR STAFF</a>
  <a style="left:354px">NEWS AND UPDATES</a>
  <a style="left:486px">CORPORATE WELLNESS</a>
  <a style="left:627px">FORMS</a>
  <a style="left:692px">CONTACT</a>
</nav>

<!-- hero -->
<section class="abs hero">
  <div class="hero-photo" role="img" aria-label="Therapist guiding a smiling woman through a resistance band shoulder stretch"></div>
  <h1 class="abs hero-title">WELCOME TO<br><span>THORNLEIGH VITALITY CENTRE</span></h1>
  <p class="abs hero-copy">There are many variations of passages of Lorem Ipsum available, but the majority have suffered alteration in some form, by injected humour,</p>
  <div class="abs btn-solid hero-btn">BOOK AN APPOINTMENT</div>
  <div class="abs hero-dots"><i></i><i class="on"></i><i></i></div>
</section>

<!-- about -->
<div class="abs about-photo" role="img" aria-label="Smiling doctor in a white coat with a stethoscope, arms crossed"></div>
<h2 class="abs about-kicker">ABOUT</h2>
<h2 class="abs about-title">THORNLEIGH VITALITY CENTRE</h2>
<div class="abs about-rule"></div>
<div class="abs about-copy">
  <p>Established in 1989 the Thornleigh Vitality Centre has become one of Canada's leaders in providing quality care and innovative wellness programs for the community. The founder and director Dr. Alden Marrow's vision has come to life with over 30 practitioners providing a multitude of different services under one roof. Some of the services include Chiropractic, Physiotherapy, Athletic Therapy, Naturopathy, Massage Therapy, Acupuncture and Personal Training.</p>
  <p>The Thornleigh Vitality Centre has a complete Pilates studio on its premises. We also offer many wellness seminars free of cost to the public. Our Centre is committed to helping improve and extend the lives of as many people as possible in our community. Come and join our family and start changing your life today.</p>
</div>
<div class="abs btn-outline about-btn">GET AN APPOINTMENT</div>

<!-- services -->
<section class="abs services">
  <h2 class="section-head">OUR SERVICES</h2>
  <div class="head-rule"></div>

  <div class="service" style="left:21px">
    <div class="service-icon"><svg width="40" height="40" viewBox="0 0 40 40" fill="none" stroke="#fff" stroke-width="2"><rect x="6" y="22" width="28" height="5" rx="2"/><path d="M10 27v7M30 27v7M12 18h16"/></svg></div>
    <h3>CHIROPRACTIC</h3>
    <ul><li>Adjustment</li><li>Functional Adjustment</li><li>Custom Orthotics and</li><li>Bracing</li></ul>
  </div>
  <div class="service" style="left:162px">
    <div class="service-icon"><svg width="40" height="40" viewBox="0 0 40 40" fill="none" stroke="#fff" stroke-width="2"><path d="M10 32h20M14 32V18h12v14M20 8v10"/></svg></div>
    <h3>PHYSIOTHERAPY</h3>
    <ul><li>Physiotherapy</li><li>Athletic Therapy</li><li>Custom Orthotics and</li><li>Bracing</li></ul>
  </div>
  <div class="service" style="left:299px">
    <div class="service-icon"><svg width="40" height="40" viewBox="0 0 40 40" fill="none" stroke="#fff" stroke-width="2"><path d="M6 20h4M30 20h4M10 14v12M30 14v12M10 20h20"/></svg></div>
    <h3>ACTIVE<br>REHABILITATION</h3>
    <ul><li>Personal Training</li><li>Pilates</li><li>Fascial Stretch Therapy</li><li>Alexander Technique</li><li>Qigong</li></ul>
  </div>
  <div class="service" style="left:437px">
    <div class="service-icon"><svg width="40" height="40" viewBox="0 0 40 40" fill="#fff"><ellipse cx="20" cy="12" rx="9" ry="4"/><ellipse cx="20" cy="21" rx="11" ry="4"/><ellipse cx="20" cy="30" rx="13" ry="4"/></svg></div>
    <h3>MASSAGE THERAPY</h3>
    <ul><li>Swedish Massage</li><li>Hot Stone Massage</li><li>Sports Massage</li><li>Shiatsu Massage</li><li>Pregnancy Massage</li><li>Thai Massage</li><li>Foot Reflexology</li><li>Infant Massage</li></ul>
  </div>
  <div class="service" style="left:576px">
    <div class="service-icon"><svg width="40" height="40" viewBox="0 0 40 40" fill="none" stroke="#fff" stroke-width="2"><rect x="9" y="7" width="22" height="26" rx="2"/><path d="M14 22c0-4 3-7 6-7s6 3 6 7zM13 27h14"/></svg></div>
    <h3>NUTRITION AND<br>LIFESTYLE MEDICINE</h3>
    <ul><li>Naturopathy</li><li>Traditional Chinese</li><li>Medicine</li><li>Acupuncture</li><li>Varicose Vein Injections</li><li>Certified Hypnotherapist</li></ul>
  </div>
  <div class="service" style="left:706px">
    <div class="service-icon"><svg width="40" height="40" viewBox="0 0 40 40" fill="#fff"><rect x="17" y="5" width="6" height="5" rx="1"/><rect x="17" y="12" width="6" height="5" rx="1"/><rect x="17" y="19" width="6" height="5" rx="1"/><path d="M8 26c4 0 8 2 12 6 4-4 8-6 12-6l-2 6H10z"/></svg></div>
    <h3>OSTEOPATHY</h3>
    <ul><li>Osteopathic</li><li>Manual</li><li>Practitioner</li></ul>
  </div>
</section>

<!-- partners -->
<h2 class="abs section-head partners-head">OUR PARTNERS</h2>
<div class="abs head-rule partners-rule"></div>
<div class="abs partner" style="left:244px" role="img" aria-label="Partner badge"><span class="partner-shape"></span></div>
<div class="abs partner" style="left:497px" role="img" aria-label="Partner badge"><span class="partner-shape"></span></div>
<div class="abs partner" style="left:755px" role="img" aria-label="Partner badge"><span class="partner-shape"></span></div>

<!-- wellness fair banner -->
<section class="abs banner">
  <div class="banner-photo" role="img" aria-label="Smiling woman with glasses in a light blue shirt"></div>
  <svg class="banner-cut" width="92" height="44" viewBox="0 0 92 44"><polygon points="0,0 92,0 0,44" fill="#fff"/></svg>
  <div class="banner-copy">
    <p>Our Centre is committed to helping improve and extend the lives of as many people as possible in our community.</p>
    <p class="join">COME AND JOIN OUR FAMILY AND START CHANGING YOUR LIFE TODAY</p>
    <h2>PLANNING A WELLNESS FAIR?<br>WE CAN HELP!</h2>
    <p class="mail">CONTACT US AT <u>INFO@THORNLEIGHVITALITY.EXAMPLE</u> FOR MORE DETAILS.</p>
  </div>
</section>

<!-- blog -->
<div class="abs blog-head"><b>"</b>FROM THE BLOG</div>
<div class="abs hours">
  <h4>Labour Day Weekend Hours</h4>
  <ul>
    <li>Sat, September 2nd, 2017 – Open 09:00am – 05:00pm</li>
    <li>Sun, September 3rd, 2017 – Open 10:00am – 05:00pm</li>
    <li class="closed">Mon, September 4th, 2017 – Closed</li>
    <li>Tue, September 5th, 2017 – Open 07:30am – 05:00pm</li>
  </ul>
</div>
<h3 class="abs post-title">THINK WELL PROGRAM</h3>
<p class="abs post-date">Monday, June 5, 2017 – 09:29</p>
<p class="abs post-copy">Did you know that your mental wellness can directly affect your physical wellness, and vice versa? Our Think Well program comprises Counselling and Sleep Therapy to help you address stress, sleep hygiene, anxiety, depression, family relationships, life transitions, bereavement, and more</p>
<div class="abs btn-outline post-btn">Read More</div>

<div class="abs divider" style="top:2096px"></div>

<!-- reviews -->
<div class="abs review" style="left:267px">
  <span class="name">Zintrel</span>
  <span class="label">Reviews <span class="stars muted">★★★★★</span></span>
</div>
<div class="abs review" style="left:505px">
  <span class="name">Quorva</span>
  <span class="label">Reviews <span class="stars">★★★★★</span></span>
</div>
<div class="abs review" style="left:737px">
  <span class="name" style="font-size:13px;line-height:18px">thornleigh vitality</span>
  <span class="label">Reviews <span class="stars">★★★★★</span></span>
</div>

<div class="abs divider" style="top:2260px"></div>

<!-- testimonial -->
<div class="abs patient-photo" role="img" aria-label="Happy young woman giving a thumbs up"></div>
<h2 class="abs patients-title">HAPPY PATIENTS</h2>
<div class="abs patients-rule"></div>
<div class="abs quote-mark">"</div>
<p class="abs patients-copy">I attended your clinic recently and was surprised. I am 68 years old and never before was I received so warmly. I believe that natural medicine is the best medicine for all of us. It has fewer and more benign side effects than those created in labs. Your clinic I dream will be the future of health care. My regret is that most patients are misled by the medical and pharmaceutical powers that be to sway their minds to traditional methods of treating their conditions. I wish all of you well in your endeavors</p>
<p class="abs patients-sign">Regards Milo</p>

<!-- footer -->
<footer class="abs footer">
  <div class="footer-col footer-about">
    <p>Lorem ipsum dolor sit amet, consectetur adipisci elit. Sed et elementum nulla, eu placerat felis. Et mtin orci lacus, id varius.<br>Call Us At: Mail Us At: Our Location:</p>
    <div class="contact-rows">
      <span>Call Us</span><span>: +100 55 501 - (+00) 555 01 234</span>
      <span>Our Location</span><span>: hello@thornleigh.example - desk@thornleigh.example</span>
      <span>Our Location</span><span>: #No, Street Name, Locality, Landmark,<br>&nbsp;&nbsp;City, Zip code 12345</span>
    </div>
  </div>
  <div class="footer-col" style="left:429px;top:42px">
    <h5>Useful Links</h5>
    <ul class="links"><li>Emergency Care</li><li>Emergency Care</li><li>Doctors Community</li><li>Emergency Care</li><li>Emergency Care</li></ul>
  </div>
  <div class="footer-col" style="left:611px;top:42px;width:200px">
    <h5>Our Newsletter</h5>
    <p>Nunc ut volutpat ex. Morbi risus elit, mattis in mi ne mollis blandit erat.</p>
    <div class="field" style="margin-top:14px">Your Name</div>
    <div class="field">Your E-Mail</div>
    <div class="subscribe">Subscribe</div>
  </div>
  <div class="footer-bottom">Copyright lumenvalemedical@2017. All rights are reserved</div>
</footer>

</body>
</html>
```